COBALT YARDS needs bisness cards pronto

Bisness name is "COBALT YARDS" new bisness the bisness includes lawn mowing, garden matanace, and any jobs around the house.
I need a card that is colorful and vibrant and the bisness of lawn mowing maybe with some nature with it. It also needs my contact details"Desmond Larkwell mobile 0412563049 call for free quote and email gwen.brookvale@fernmail.com and a catchy tag line

Requirements
Must have
• Bisness name "COBALT YARDS"
Contact details "0412563049"
Email gwen.brookvale@fernmail.com
Call for free quote

```html
<!DOCTYPE html>
<html lang="en">
<head>
<meta charset="utf-8">
<title>Cobalt Yards Business Card</title>
<link href="https://fonts.googleapis.com/css2?family=Bebas+Neue&family=Oswald:wght@200;300&display=swap" rel="stylesheet">
<style>
  :root {
    --page: #ffffff;
    --card: #000000;
    --green: #33943f;
    --green-deep: #2a7a34;
    --ink: #000000;
  }
  html, body {
    margin: 0;
    padding: 0;
    width: 1200px;
    height: 1000px;
    overflow: hidden;
    background: var(--page);
  }
  .card {
    position: absolute;
    left: 75px;
    top: 200px;
    width: 1050px;
    height: 600px;
    background: var(--card);
    overflow: hidden;
  }
  .slope {
    position: absolute;
    inset: 0;
  }
  .owner {
    position: absolute;
    left: 41px;
    top: 70px;
    margin: 0;
    font-size: 58px;
    line-height: 1;
    color: var(--green);
    letter-spacing: -1px;
    white-space: nowrap;
  }
  .owner-first {
    font-family: "Oswald", sans-serif;
    font-weight: 200;
  }
  .owner-last {
    font-family: "Bebas Neue", sans-serif;
    font-size: 66px;
  }
  .contact-bar {
    position: absolute;
    left: 0;
    height: 36px;
    background: var(--green);
    color: var(--ink);
    font-family: "Oswald", sans-serif;
    font-weight: 300;
    font-size: 31px;
    line-height: 36px;
    letter-spacing: -1px;
    padding-left: 53px;
    box-sizing: border-box;
    white-space: nowrap;
  }
  .contact-phone { top: 259px; width: 210px; }
  .contact-email { top: 316px; width: 388px; }
  .brand-name {
    position: absolute;
    left: 420px;
    top: 328px;
    margin: 0;
    font-family: "Bebas Neue", sans-serif;
    font-size: 70px;
    line-height: 1;
    color: var(--green);
    white-space: nowrap;
  }
  .mower-art {
    position: absolute;
    left: 775px;
    top: 140px;
    width: 260px;
    height: 240px;
    border-radius: 6px;
    background: linear-gradient(160deg, var(--green) 0%, var(--green-deep) 100%);
  }
  .cta {
    position: absolute;
    right: 47px;
    top: 516px;
    margin: 0;
    font-family: "Bebas Neue", sans-serif;
    font-size: 52px;
    line-height: 1;
    color: var(--ink);
    white-space: nowrap;
  }
</style>
</head>
<body>
  <main class="card">
    <svg class="slope" width="1050" height="600" viewBox="0 0 1050 600" aria-hidden="true">
      <polygon points="250,600 1050,352 1050,600" fill="var(--green)"/>
    </svg>

    <h1 class="owner"><span class="owner-first">DESMOND</span> <span class="owner-last">LARKWELL</span></h1>

    <div class="contact-bar contact-phone">0412563049</div>
    <div class="contact-bar contact-email">gwen.brookvale@fernmail.com</div>

    <p class="brand-name">COBALT YARDS</p>
    <div class="mower-art" role="img" aria-label="Illustration of a lawn mower cutting grass on a slope"></div>

    <p class="cta">CALL FOR FREE QUOTE</p>
  </main>
</body>
</html>
```